Business cards — need something that creates “wow” factor

Need a sleek and clean looking business card. Something that is clear and consise. These business cards are for my painting business and hundreds will be placed in the Dallas area between all Halverd Pemberton paint stored. These card really need to stick out! Open to any and all ideas...

Target Market(s)

Residential clientele

Industry/Entity Type

Painting

Contact Information for Business Card

Dorian Vakelby
Owner

382.516.2074

Web: Mesahuepainting.example (still under construction)
Mesahuepainting@mailbox.example

Font styles to use
Sans Serif

Colors

Designer to choose colors to be used in the design.

Requirements
Must have
• My name, number, website, email, Socialpage
• and “100% customer satisfaction guaranteed”
• Socialpage.example/Mesahuepainting/
Nice to have
• Listed services
• Interior/exterior painting
• Drywall repair/texture
• Fence staining/refinishing
• Concrete staining
• Epoxy flooring
• Pressure washing

```html
<!DOCTYPE html>
<html lang="en">
<head>
<meta charset="utf-8">
<title>Mesa Hue Painting — Business Card</title>
<link rel="stylesheet" href="https://fonts.googleapis.com/css2?family=Lato:wght@400;700;900&display=swap">
<style>
  :root {
    --page: #f1f1f1;
    --paper: #ffffff;
    --ink: #111111;
    --night: #050505;
    --red: #d9213a;
    --red-fold: #8e1022;
    --orange: #f47b20;
    --green: #8dc63f;
    --blue: #0f8fd6;
    --blue-fold: #0a5d8d;
    --stroke-grey: #d2d2d2;
    --check: #2d6fb8;
    --white: #ffffff;
  }
  * { box-sizing: border-box; margin: 0; padding: 0; }
  html, body {
    width: 1200px; height: 1200px; overflow: hidden;
    background: var(--page);
    font-family: "Lato", Arial, sans-serif;
  }
  .card {
    position: absolute; left: 193px; width: 863px; height: 493px;
    background: var(--paper); overflow: hidden;
  }
  .card--front { top: 76px; }
  .card--back { top: 627px; }

  /* Front */
  .front-dark {
    position: absolute; left: 427px; top: 0; right: 0; bottom: 0;
    background: var(--night);
  }
  .brush-art {
    position: absolute; left: 560px; top: 170px; width: 303px; height: 250px;
    background: radial-gradient(ellipse at 55% 60%, #2a2f33 0%, #15181a 45%, rgba(5,5,5,0) 75%);
  }
  .brand {
    position: absolute; display: flex; align-items: center; gap: 12px;
    font-weight: 900; color: var(--ink); letter-spacing: 1px; white-space: nowrap;
  }
  .brand__mark { display: block; background: var(--red); }
  .brand--front { left: 100px; top: 222px; font-size: 42px; }
  .brand--front .brand__mark { width: 28px; height: 28px; }
  .brand--back { left: 340px; top: 92px; font-size: 28px; }
  .brand--back .brand__mark { width: 18px; height: 18px; }

  .tab {
    position: absolute; width: 97px;
    display: flex; align-items: center; justify-content: center;
  }
  .tab__icon { width: 38px; height: 38px; }
  .tab__icon .solid { fill: var(--white); stroke: none; }
  .tab__icon .line { fill: none; stroke: var(--white); stroke-width: 1.6; }
  .tab--red { background: var(--red); }
  .tab--orange { background: var(--orange); }
  .tab--green { background: var(--green); }
  .tab--blue { background: var(--blue); }
  .front-tabs .tab { left: 395px; }
  .fold { position: absolute; width: 0; height: 0; }
  .fold--front-top {
    left: 395px; top: 37px;
    border-left: 32px solid transparent; border-bottom: 12px solid var(--red-fold);
  }
  .fold--front-bottom {
    left: 395px; top: 444px;
    border-left: 32px solid transparent; border-top: 12px solid var(--blue-fold);
  }

  .contact { position: absolute; left: 510px; color: var(--white); white-space: nowrap; }
  .contact__name { top: 42px; font-size: 33px; letter-spacing: 0.5px; line-height: 1; }
  .contact__name strong { font-weight: 900; }
  .contact__name span { font-weight: 400; }
  .contact__role { top: 82px; font-size: 24px; font-weight: 400; }
  .contact__line { font-size: 20px; font-weight: 400; }

  /* Back */
  .side { position: absolute; top: 0; bottom: 0; width: 64px; background: var(--night); }
  .side--left { left: 0; }
  .side--right { right: 0; }
  .back-tabs .tab { width: 65px; }
  .back-tabs--left .tab { left: 31px; }
  .back-tabs--right .tab { left: 764px; }
  .fold--back-left {
    left: 31px; top: 39px;
    border-left: 32px solid transparent; border-bottom: 12px solid var(--red-fold);
  }
  .fold--back-right {
    left: 798px; top: 39px;
    border-right: 32px solid transparent; border-bottom: 12px solid var(--red-fold);
  }
  .stroke-texture {
    position: absolute; left: 207px; top: 27px; width: 453px; height: 400px;
    background: linear-gradient(90deg, rgba(210,210,210,0.3) 0%, var(--stroke-grey) 20%, var(--stroke-grey) 70%, rgba(210,210,210,0.2) 100%);
  }
  .services {
    position: absolute; left: 247px; top: 196px; list-style: none;
  }
  .services li {
    display: flex; align-items: center; gap: 14px;
    height: 34px; font-size: 20px; font-weight: 700; color: var(--ink);
    letter-spacing: 0.2px;
  }
  .services svg { width: 15px; height: 15px; fill: none; stroke: var(--check); stroke-width: 3; }
  .guarantee {
    position: absolute; left: 64px; right: 64px; top: 418px;
    text-align: center; font-size: 25px; font-weight: 900; color: var(--ink);
    letter-spacing: 0.3px;
  }
  .social {
    position: absolute; left: 64px; right: 64px; top: 455px;
    text-align: center; font-size: 17px; font-weight: 400; color: var(--ink);
  }
</style>
</head>
<body>

<section class="card card--front">
  <div class="brand brand--front"><span class="brand__mark"></span>Mesa Hue</div>
  <div class="front-dark"></div>
  <div class="brush-art" role="img" aria-label="Paintbrush with dark paint splatter"></div>

  <div class="front-tabs">
    <span class="fold fold--front-top"></span>
    <div class="tab tab--red" style="top:49px;height:99px">
      <svg class="tab__icon" viewBox="0 0 24 24"><circle class="solid" cx="12" cy="8" r="4.5"/><path class="solid" d="M3 22c0-5 4-8 9-8s9 3 9 8z"/></svg>
    </div>
    <div class="tab tab--orange" style="top:148px;height:100px">
      <svg class="tab__icon" viewBox="0 0 24 24"><path class="solid" d="M3 7c0-2 2-3 9-3s9 1 9 3v2h-5V7H8v2H3z"/><path class="solid" d="M6 11h12l2 9H4z"/><rect x="9" y="13" width="6" height="5" fill="#f47b20"/></svg>
    </div>
    <div class="tab tab--green" style="top:248px;height:97px">
      <svg class="tab__icon" viewBox="0 0 24 24"><circle class="line" cx="12" cy="12" r="9"/><ellipse class="line" cx="12" cy="12" rx="4" ry="9"/><path class="line" d="M3 12h18M5 7h14M5 17h14"/></svg>
    </div>
    <div class="tab tab--blue" style="top:345px;height:99px">
      <svg class="tab__icon" viewBox="0 0 24 24"><path class="solid" d="M2 5h20v14H2z"/><path d="M2 5l10 8 10-8" fill="none" stroke="#0f8fd6" stroke-width="1.6"/></svg>
    </div>
    <span class="fold fold--front-bottom"></span>
  </div>

  <p class="contact contact__name"><strong>DORIAN</strong> <span>VAKELBY</span></p>
  <p class="contact contact__role">OWNER</p>
  <p class="contact contact__line" style="top:172px">382.516.2074</p>
  <p class="contact contact__line" style="top:270px">Mesahuepainting.example</p>
  <p class="contact contact__line" style="top:366px">Mesahuepainting@mailbox.example</p>
</section>

<section class="card card--back">
  <div class="side side--left"></div>
  <div class="side side--right"></div>

  <div class="back-tabs back-tabs--left">
    <span class="fold fold--back-left"></span>
    <div class="tab tab--red" style="top:51px;height:98px"></div>
    <div class="tab tab--orange" style="top:149px;height:99px"></div>
    <div class="tab tab--green" style="top:248px;height:97px"></div>
    <div class="tab tab--blue" style="top:345px;height:99px"></div>
  </div>
  <div class="back-tabs back-tabs--right">
    <span class="fold fold--back-right"></span>
    <div class="tab tab--red" style="top:51px;height:98px"></div>
    <div class="tab tab--orange" style="top:149px;height:99px"></div>
    <div class="tab tab--green" style="top:248px;height:97px"></div>
    <div class="tab tab--blue" style="top:345px;height:99px"></div>
  </div>

  <div class="stroke-texture" role="img" aria-label="Grey dry-brush paint stroke texture"></div>
  <div class="brand brand--back"><span class="brand__mark"></span>Mesa Hue</div>

  <ul class="services">
    <li><svg viewBox="0 0 16 16"><path d="M2 8l4 4 8-9"/></svg>INTERIOR/EXTERIOR PAINTING</li>
    <li><svg viewBox="0 0 16 16"><path d="M2 8l4 4 8-9"/></svg>DRYWALL REPAIR/TEXTURE</li>
    <li><svg viewBox="0 0 16 16"><path d="M2 8l4 4 8-9"/></svg>FENCE STAINING/REFINISHING</li>
    <li><svg viewBox="0 0 16 16"><path d="M2 8l4 4 8-9"/></svg>CONCRETE STAINING</li>
    <li><svg viewBox="0 0 16 16"><path d="M2 8l4 4 8-9"/></svg>EPOXY FLOORING</li>
    <li><svg viewBox="0 0 16 16"><path d="M2 8l4 4 8-9"/></svg>PRESSURE WASHING</li>
  </ul>

  <p class="guarantee">100% CUSTOMER SATISFACTION GUARANTEED</p>
  <p class="social">Socialpage.example/Mesahuepainting/</p>
</section>

</body>
</html>
```